business cards for roofing company

Hi guys!
I need x2 business cards - one for workers and one for general business

Information for general business card:
front side:
- logo in the files + motto "Quality from the Ground Up" under Facades in freestyle script regular
- colors - like in the logo #C9F701 & #001C42
- INFORMATION text: Contact Us Today and Get Free Quote & Advice!
- Phone number (555) 208-4417
- e-mail: info@ brightlinefacades.us ( skip spaces after @)
- website: brightlinefacades.us
- address:
4871 Thistlemoor Court
Naperville, IL 60999

other side:
SERVICES:
As an experienced company, we offer:
- Roofing
- Siding
- Windows
Installation, Replacement & Repair!

-----------------------------------------------------------------------------------

Information for business cards for workers:
front side:
Worker information:
Tobias Grunholt
General Manager
phone:
C – (555) 391-0586
O – (555) 208-4417
generalmanager@ brightlinefacades.us ( skip spaces after @)
address:
4871 Thistlemoor Court
Naperville, IL 60999

another side:
SERVICES:
- Roofing
- Siding
- Windows

In the files, I also put some photos of services & logo

Need it in US size standards (3.5" X 2") + 1/8" Bleed Area - All Around (e.g. Designing a 3.5"x2" business card? The file you submit should be 3.625"x2.125") to print
in png, ai, pdf, PSD, jpg file

```html
<!DOCTYPE html>
<html lang="en">
<head>
<meta charset="utf-8">
<title>Brightline Facades – Business Cards</title>
<link href="https://fonts.googleapis.com/css2?family=Montserrat:wght@400;500;600;700;800&display=swap" rel="stylesheet">
<style>
  :root {
    --lime: #c9f701;
    --lime-soft: #c6e43a;
    --navy: #001c42;
    --navy-deep: #0d1f4a;
    --navy-muted: #3a4a66;
    --white: #ffffff;
    --band-grey: #e9ebe8;
    --ink: #1c2540;
    --backdrop: #e6e6e4;
  }
  * { box-sizing: border-box; margin: 0; padding: 0; }
  html, body {
    width: 1200px; height: 856px; overflow: hidden;
    background: var(--backdrop);
    font-family: "Montserrat", Arial, sans-serif;
    color: var(--ink);
  }
  .canvas { position: relative; width: 1200px; height: 856px; }

  .card {
    position: absolute;
    width: 540px; height: 309px;
    background: var(--white);
    overflow: hidden;
    box-shadow: 0 14px 28px rgba(0,0,0,0.18);
  }
  .card--front { left: 40px; top: 190px; }
  .card--back { left: 620px; top: 356px; }

  .card__shapes { position: absolute; inset: 0; }

  /* brand lockup */
  .brand { position: absolute; display: flex; align-items: center; gap: 10px; }
  .brand__mark { width: 20px; height: 20px; background: var(--navy); flex: none; }
  .brand__name {
    font-weight: 800; color: var(--navy); text-transform: uppercase;
    line-height: 1.02; letter-spacing: 0.5px;
  }
  .card--front .brand { left: 34px; top: 156px; }
  .card--front .brand__name { font-size: 21px; }
  .card--back .brand { left: 24px; top: 24px; gap: 8px; }
  .card--back .brand__mark { width: 15px; height: 15px; }
  .card--back .brand__name { font-size: 14px; }

  /* front card contact block */
  .person { position: absolute; left: 300px; top: 24px; color: var(--navy); }
  .person__name { font-size: 19px; letter-spacing: 0.5px; text-transform: uppercase; line-height: 1.2; }
  .person__name strong { font-weight: 800; }
  .person__name span { font-weight: 500; }
  .person__role { font-size: 9px; color: var(--navy-muted); margin-top: 1px; }

  .contact { position: absolute; left: 300px; list-style: none; }
  .contact__item { display: flex; align-items: center; gap: 9px; font-size: 10px; line-height: 1.25; }
  .contact__icon {
    width: 18px; height: 18px; border-radius: 50%;
    display: flex; align-items: center; justify-content: center; flex: none;
  }
  .contact--on-lime { top: 68px; color: var(--navy); }
  .contact--on-lime .contact__icon { background: var(--navy); }
  .contact--on-lime .contact__item { margin-bottom: 9px; }
  .contact--on-navy { top: 160px; color: var(--white); }
  .contact--on-navy .contact__item { margin-bottom: 15px; }
  .contact--on-navy .contact__icon { background: var(--lime); }

  /* back card */
  .services { position: absolute; right: 26px; top: 28px; text-align: right; }
  .services__title { font-size: 15px; font-weight: 500; color: var(--navy); letter-spacing: 0.5px; }
  .services__lead { font-size: 9.5px; color: var(--ink); margin-top: 1px; }

  .band-grey { position: absolute; left: 0; right: 0; top: 150px; height: 110px; background: var(--band-grey); }
  .band-lime { position: absolute; left: 0; right: 0; bottom: 0; height: 30px; background: var(--lime-soft); }

  .photo { position: absolute; top: 82px; height: 118px; }
  .photo--roofing { left: 0; width: 168px; background: linear-gradient(160deg, #b9c9d6 0%, #8e8578 55%, #5d5a55 100%); }
  .photo--siding { left: 186px; width: 150px; background: linear-gradient(170deg, #9fbde0 0%, #e8e4da 50%, #8b7a66 100%); }
  .photo--windows { left: 358px; width: 182px; height: 126px; background: linear-gradient(90deg, #9fb88a 0%, #d9e3d2 55%, #f3f3f1 100%); }

  .service-label { position: absolute; font-size: 10px; color: var(--ink); }
  .service-label--roofing { left: 60px; top: 210px; }
  .service-label--siding { left: 230px; top: 214px; }
  .service-label--windows { left: 430px; top: 240px; }
  .tagline { position: absolute; left: 170px; top: 236px; font-size: 10px; color: var(--ink); }
</style>
</head>
<body>
<main class="canvas">

  <section class="card card--front" aria-label="Business card, contact side">
    <svg class="card__shapes" viewBox="0 0 540 309" aria-hidden="true">
      <polygon points="60,0 540,0 540,140 300,140" fill="var(--lime)"/>
      <polygon points="300,140 540,140 540,309 170,309" fill="var(--navy-deep)"/>
    </svg>

    <div class="brand">
      <span class="brand__mark"></span>
      <span class="brand__name">Brightline<br>Facades</span>
    </div>

    <div class="person">
      <p class="person__name"><strong>Tobias</strong> <span>Grunholt</span></p>
      <p class="person__role">General Manager</p>
    </div>

    <ul class="contact contact--on-lime">
      <li class="contact__item">
        <span class="contact__icon">
          <svg width="10" height="10" viewBox="0 0 24 24"><path fill="var(--lime)" d="M6.6 10.8a15.1 15.1 0 0 0 6.6 6.6l2.2-2.2c.3-.3.7-.4 1-.2 1.1.4 2.3.6 3.6.6.6 0 1 .4 1 1V20c0 .6-.4 1-1 1A17 17 0 0 1 3 4c0-.6.4-1 1-1h3.5c.6 0 1 .4 1 1 0 1.3.2 2.5.6 3.6.1.3 0 .7-.2 1l-2.3 2.2z"/></svg>
        </span>
        <span>(555) 391-0586<br>(555) 208-4417</span>
      </li>
      <li class="contact__item">
        <span class="contact__icon">
          <svg width="10" height="10" viewBox="0 0 24 24" fill="none" stroke="var(--lime)" stroke-width="2"><circle cx="12" cy="12" r="9"/><path d="M3 12h18M12 3c3 3 3 15 0 18M12 3c-3 3-3 15 0 18"/></svg>
        </span>
        <span>www.brightlinefacades.us</span>
      </li>
    </ul>

    <ul class="contact contact--on-navy">
      <li class="contact__item">
        <span class="contact__icon">
          <svg width="10" height="10" viewBox="0 0 24 24"><rect x="3" y="6" width="18" height="12" fill="var(--navy)"/><path d="M3 6l9 7 9-7" fill="none" stroke="var(--lime)" stroke-width="1.6"/></svg>
        </span>
        <span>info@brightlinefacades.us</span>
      </li>
      <li class="contact__item">
        <span class="contact__icon">
          <svg width="10" height="10" viewBox="0 0 24 24"><path fill="var(--navy)" d="M12 2a7 7 0 0 0-7 7c0 5 7 13 7 13s7-8 7-13a7 7 0 0 0-7-7zm0 9.5a2.5 2.5 0 1 1 0-5 2.5 2.5 0 0 1 0 5z"/></svg>
        </span>
        <span>4871 Thistlemoor Court<br>Naperville IL 60999</span>
      </li>
    </ul>
  </section>

  <section class="card card--back" aria-label="Business card, services side">
    <div class="band-grey"></div>
    <div class="band-lime"></div>

    <div class="brand">
      <span class="brand__mark"></span>
      <span class="brand__name">Brightline<br>Facades</span>
    </div>

    <div class="services">
      <p class="services__title">SERVICES:</p>
      <p class="services__lead">As an experienced company, we offer</p>
    </div>

    <div class="photo photo--roofing" role="img" aria-label="Photo of a house roof with shingles and gables"></div>
    <div class="photo photo--siding" role="img" aria-label="Photo of a two-storey house with new siding"></div>
    <div class="photo photo--windows" role="img" aria-label="Photo of an open white window frame"></div>

    <p class="service-label service-label--roofing">Roofing</p>
    <p class="service-label service-label--siding">siding</p>
    <p class="service-label service-label--windows">windows</p>
    <p class="tagline">Installation, Replacement &amp; Repair</p>
  </section>

</main>
</body>
</html>
```